new KVR one page flyer

We need a 1 page A4 size flyer (need it asap please) that describes on 1 page with art work and using photos the services we provide. I have included some examples of old previous flyers from our other (seperate divisions of the business) I have named a photo called (photo for top of design) however you do your design this photo needs to be the star of the page by either having it at the top or bottom of the page please and we usually like this photo to be in greyscale colour.
we do like greyscale designs but are open to see what you come up with as a whole page of grey white and black might not suit.

Needs to list the following

Services include:
Over size loads / Hot Shot Loads
Heavy Vehicle Recovery services
Potable Water Deliveries
Road Building / Maintenance
Earthworks
Sand & Metal Supply & Cartage
Road Train Tippers
Road Train Tankers
Road Train Flat Tops
Drop Deck Trailers
Mine site accredited equipment & Operators.

We offer a large rage of services not listed so call us today for a personalised quote to suit your needs.

To go on the bottom of the page our contact details are

KVR Pty Ltd
Depot: Lot 514, Banksia Flats Track Coober Pedy
Mobile: 047 216 9381
email: darren@kestrelvaleroadworks.com.au

Target Market(s)

new clients

Colors

Designer to choose colors to be used in the design.

Requirements
Must have
• our services listed
Nice to have
• stand out designs

```html
<!DOCTYPE html>
<html lang="en">
<head>
<meta charset="utf-8">
<title>KVR Pty Ltd – Services Flyer</title>
<link rel="stylesheet" href="https://fonts.googleapis.com/css2?family=Arimo:wght@400;700&family=Barlow:wght@800;900&family=Baloo+2:wght@800&display=swap">
<style>
  :root {
    --backdrop: #4d4d4d;
    --ink-black: #0f0f11;
    --panel-slate: #3a3a40;
    --brand-blue: #3d4fc4;
    --accent-blue: #4a63f0;
    --silver: #b9b9bd;
    --text-light: #ececf0;
    --text-dark: #111114;
  }
  * { margin: 0; padding: 0; box-sizing: border-box; }
  html, body { width: 1031px; height: 1200px; overflow: hidden; background: var(--backdrop); }
  .flyer {
    position: absolute; left: 158px; top: 87px;
    width: 741px; height: 1047px; overflow: hidden;
    background: var(--panel-slate);
    font-family: "Arimo", Arial, sans-serif;
  }
  .header { position: absolute; left: 0; top: 0; width: 741px; height: 149px; }
  .header svg, .footer svg { position: absolute; left: 0; top: 0; }
  .brand-name {
    position: absolute; left: 52px; top: 22px;
    font-family: "Barlow", Arial, sans-serif; font-weight: 900;
    font-size: 92px; line-height: 1; letter-spacing: 2px;
    color: var(--silver);
  }
  .contact-block { position: absolute; left: 430px; top: 30px; width: 300px; text-align: right; }
  .contact-title {
    font-family: "Barlow", Arial, sans-serif; font-weight: 900;
    font-size: 38px; line-height: 1; color: #fff; letter-spacing: 0.5px;
  }
  .contact-phone {
    margin-top: 10px; display: flex; justify-content: flex-end; align-items: center; gap: 6px;
    font-family: "Barlow", Arial, sans-serif; font-weight: 900;
    font-size: 36px; line-height: 1; color: var(--text-dark);
  }
  .hero-photo {
    position: absolute; left: 0; top: 149px; width: 741px; height: 304px;
    background: linear-gradient(180deg, #d8d8d8 0%, #a9a9a9 35%, #4a4a4a 62%, #8a8a8a 80%, #b4b4b4 100%);
  }
  .services-heading {
    position: absolute; left: 0; top: 389px; width: 259px; height: 54px;
    background: #15173a; border-bottom: 2px solid var(--brand-blue);
    font-family: "Barlow", Arial, sans-serif; font-weight: 900;
    font-size: 30px; color: #fff; line-height: 54px; padding-left: 33px;
    text-shadow: 2px 2px 3px #000;
  }
  .services-panel { position: absolute; left: 0; top: 453px; width: 741px; height: 480px; background: var(--panel-slate); }
  .service-list {
    position: absolute; left: 58px; top: 468px; width: 360px;
    list-style: disc; color: var(--text-light);
    font-size: 20px; line-height: 27.6px;
  }
  .divider { position: absolute; left: 44px; top: 814px; width: 363px; height: 4px; background: var(--accent-blue); }
  .cta-note {
    position: absolute; left: 36px; top: 834px; width: 400px;
    font-size: 14px; font-weight: 700; line-height: 19px; color: #fff; text-transform: uppercase;
  }
  .cta-quote {
    position: absolute; left: 38px; top: 878px;
    font-family: "Baloo 2", Arial, sans-serif; font-weight: 800; font-style: italic;
    font-size: 27px; line-height: 1.2; color: var(--accent-blue); text-transform: uppercase;
  }
  .fleet-photo {
    position: absolute; left: 451px; width: 275px; height: 166px;
    background: linear-gradient(180deg, #4f86d1 0%, #9fbbdc 40%, #3b3b3e 62%, #a8603f 82%, #c47a53 100%);
  }
  .fleet-photo.one { top: 394px; }
  .fleet-photo.two { top: 571px; background: linear-gradient(180deg, #b9c3d1 0%, #8d97a6 35%, #2a2a2c 60%, #a26c4c 85%, #b98060 100%); }
  .fleet-photo.three { top: 747px; background: linear-gradient(180deg, #2f74cf 0%, #7fb2e6 45%, #5a5048 62%, #b85f3c 80%, #c9744f 100%); }
  .footer { position: absolute; left: 0; top: 933px; width: 741px; height: 114px; }
  .footer-address {
    position: absolute; left: 43px; top: 14px; width: 260px;
    font-size: 18px; line-height: 26px; color: var(--text-light);
  }
  .footer-contact {
    position: absolute; left: 354px; top: 40px;
    font-size: 18px; line-height: 28px; color: var(--text-light); white-space: nowrap;
  }
</style>
</head>
<body>
<main class="flyer">
  <header class="header">
    <svg width="741" height="149" viewBox="0 0 741 149">
      <rect width="741" height="149" fill="#0f0f11"/>
      <polygon points="482,0 741,0 741,149 354,149" fill="#3d4fc4"/>
      <polygon points="464,0 482,0 354,149 336,149" fill="#b9b9bd"/>
    </svg>
    <div class="brand-name">KVR</div>
    <div class="contact-block">
      <div class="contact-title">CONTACT US</div>
      <div class="contact-phone">
        <svg width="38" height="38" viewBox="0 0 24 24" aria-hidden="true"><path fill="#fff" d="M6.6 10.8a15.1 15.1 0 0 0 6.6 6.6l2.2-2.2c.3-.3.7-.4 1-.2 1.1.4 2.3.6 3.6.6.6 0 1 .4 1 1V20c0 .6-.4 1-1 1C10.6 21 3 13.4 3 4c0-.6.4-1 1-1h3.5c.6 0 1 .4 1 1 0 1.3.2 2.5.6 3.6.1.3 0 .7-.2 1z"/></svg>
        <span>047 216 9381</span>
      </div>
    </div>
  </header>

  <div class="hero-photo" role="img" aria-label="Greyscale photo of a triple road train tipper on an outback depot track"></div>

  <section class="services-panel"></section>
  <h2 class="services-heading">OUR SERVICES</h2>
  <ul class="service-list">
    <li>Over size loads / Hot Shot Loads</li>
    <li>Heavy Vehicle Recovery services</li>
    <li>Potable Water Deliveries</li>
    <li>Road Building / Maintenance</li>
    <li>Earthworks</li>
    <li>Sand &amp; Metal Supply &amp; Cartage</li>
    <li>Road Train Tippers</li>
    <li>Road Train Tankers</li>
    <li>Road Train Flat Tops</li>
    <li>Drop Deck Trailers</li>
    <li>Mine site accredited equipment &amp; Operators.</li>
  </ul>
  <div class="divider"></div>
  <p class="cta-note">We offer a large range of services not listed so call us today for a personalised</p>
  <p class="cta-quote">Quote to suit your needs.</p>

  <div class="fleet-photo one" role="img" aria-label="Photo of prime movers parked by a dome shed under blue sky"></div>
  <div class="fleet-photo two" role="img" aria-label="Photo of two black prime movers at the depot"></div>
  <div class="fleet-photo three" role="img" aria-label="Photo of a prime mover hauling a grader on a drop deck trailer"></div>

  <footer class="footer">
    <svg width="741" height="114" viewBox="0 0 741 114">
      <rect width="741" height="114" fill="#0f0f11"/>
      <polygon points="0,0 366,0 266,114 0,114" fill="#3d4fc4"/>
      <polygon points="366,0 380,0 280,114 266,114" fill="#b9b9bd"/>
    </svg>
    <div class="footer-address">KVR Pty Ltd<br>Depot: Lot 514, Banksia Flats Track Coober Pedy</div>
    <div class="footer-contact">Mobile: 047 216 9381<br>email: darren@kestrelvaleroadworks.com.au</div>
  </footer>
</main>
</body>
</html>
```